Business Card Design Project

We need a business card design for a relatively new company called Lumen Stride. We design paddle (an outdoor winter sport primarily played in the midwest and east coast) and tennis bags for women and men. Lumen Stride is a lifestyle brand for the next generation country club goers. Our bags merge fashion with functionality and are making country club sports trendier and more fashionable.

I would like to include space for
Name: (will fill this in for employees)
Lumen Stride
Phone: (will do this)
Email:
www.lumenstride-example.net

Would also like to include Facebook and Twitter icons.
Please do not use pictures of the bags - this is just to give you an idea of what style bags we sell.

Target Market(s)

30 to 40 year old men and women - luxury market

Industry/Entity Type

Fashion

Requirements
Must have
• Would like the company logo included

```html
<!DOCTYPE html>
<html lang="en">
<head>
<meta charset="utf-8">
<title>Lumen Stride – Business Card</title>
<link href="https://fonts.googleapis.com/css2?family=Questrial&family=Arimo:wght@400;700&display=swap" rel="stylesheet">
<style>
  :root {
    --bg: #e7e5e2;
    --card-white: #ffffff;
    --card-dark: #2d2d2d;
    --ink: #1c1a1b;
    --ink-soft: #444;
    --swoosh-grey: #8a8a8a;
    --swoosh-light: #c9c9c9;
    --on-dark: #ffffff;
  }
  html, body { margin: 0; padding: 0; overflow: hidden; }
  body {
    width: 1200px; height: 1018px;
    background: var(--bg);
    font-family: "Questrial", sans-serif;
    display: flex; flex-direction: column; align-items: center;
    gap: 18px; padding-top: 20px; box-sizing: border-box;
  }
  .card {
    position: relative; width: 840px; height: 480px;
    box-shadow: 0 6px 18px rgba(0,0,0,.18);
    overflow: hidden;
  }
  .card-front { background: var(--card-white); }
  .card-back { background: var(--card-dark); color: var(--on-dark); }
  .front-wave { position: absolute; inset: 0; }

  .brand {
    position: absolute; left: 60px; top: 150px;
    display: flex; align-items: center; gap: 20px;
  }
  .brand-dot { width: 56px; height: 56px; border-radius: 50%; background: var(--ink); flex: none; }
  .brand-name { font-size: 60px; color: var(--ink); letter-spacing: 1px; line-height: 1; white-space: nowrap; }

  .person { position: absolute; left: 80px; top: 300px; }
  .person-name { font-family: "Arimo", sans-serif; font-weight: 700; font-size: 28px; color: var(--ink); margin: 0; }
  .person-title { font-family: "Arimo", sans-serif; font-size: 20px; color: var(--ink-soft); margin: 2px 0 0 20px; }

  .contact {
    position: absolute; right: 26px; top: 250px;
    list-style: none; margin: 0; padding: 0;
    font-family: "Arimo", sans-serif; font-size: 15px; color: var(--on-dark);
    text-align: right;
  }
  .contact li { display: flex; align-items: center; justify-content: flex-end; gap: 8px; margin-bottom: 10px; white-space: nowrap; }
  .contact svg { width: 14px; height: 14px; flex: none; }

  .back-brand {
    position: absolute; left: 0; right: 0; top: 120px;
    display: flex; flex-direction: column; align-items: center; gap: 20px;
  }
  .back-dot { width: 110px; height: 110px; border-radius: 50%; background: var(--on-dark); }
  .back-name { font-size: 56px; letter-spacing: 2px; }

  .follow {
    position: absolute; left: 0; right: 0; top: 350px;
    display: flex; justify-content: center; align-items: center; gap: 14px;
    font-family: "Arimo", sans-serif; font-weight: 700; font-size: 32px; letter-spacing: 1px;
  }
  .social-square { width: 44px; height: 44px; border-radius: 6px; background: #5b6f9e; }
  .social-square.alt { background: #5fb4d6; }
  .back-url {
    position: absolute; left: 0; right: 0; top: 412px; text-align: center;
    font-family: "Arimo", sans-serif; font-size: 22px; letter-spacing: 5px;
  }
</style>
</head>
<body>
  <section class="card card-front">
    <svg class="front-wave" viewBox="0 0 840 480" aria-hidden="true">
      <path d="M650,0 C590,150 570,250 440,345 C320,425 160,452 0,455 L0,480 L840,480 L840,0 Z" fill="var(--swoosh-light)"/>
      <path d="M675,0 C615,150 595,255 460,352 C340,432 170,458 0,462 L0,480 L840,480 L840,0 Z" fill="var(--swoosh-grey)"/>
      <path d="M700,0 C640,150 620,260 480,360 C360,440 180,465 0,470 L0,480 L840,480 L840,0 Z" fill="var(--card-dark)"/>
    </svg>

    <div class="brand">
      <span class="brand-dot"></span>
      <span class="brand-name">Lumen Stride</span>
    </div>

    <div class="person">
      <p class="person-name">Full Name</p>
      <p class="person-title">Title</p>
    </div>

    <ul class="contact">
      <li>
        <svg viewBox="0 0 16 16"><path d="M4 1 L6.5 4 L5 6 C6 8 8 10 10 11 L12 9.5 L15 12 L13 15 C7 14.5 1.5 9 1 3 Z" fill="currentColor"/></svg>
        000-555-0142
      </li>
      <li>
        <svg viewBox="0 0 16 16"><rect x="1" y="3" width="14" height="10" rx="1" fill="none" stroke="currentColor" stroke-width="1.5"/><path d="M1.5 3.5 L8 9 L14.5 3.5" fill="none" stroke="currentColor" stroke-width="1.5"/></svg>
        info@lumenstride-example.net
      </li>
      <li>
        <svg viewBox="0 0 16 16"><circle cx="8" cy="8" r="6.5" fill="none" stroke="currentColor" stroke-width="1.4"/><ellipse cx="8" cy="8" rx="2.8" ry="6.5" fill="none" stroke="currentColor" stroke-width="1.2"/><path d="M1.5 8 H14.5" stroke="currentColor" stroke-width="1.2"/></svg>
        www.lumenstride-example.net
      </li>
    </ul>
  </section>

  <section class="card card-back">
    <div class="back-brand">
      <span class="back-dot"></span>
      <span class="back-name">Lumen Stride</span>
    </div>
    <div class="follow">
      <span>Follow Us On</span>
      <span class="social-square"></span>
      <span class="social-square alt"></span>
    </div>
    <p class="back-url">www.lumenstride-example.net</p>
  </section>
</body>
</html>
```